Label Redesign For Hemp Oil Tincture Bottle*

I need a label redesigned for Marbleleaf Hemp, current bottle label and logo is attached. The current label doesn't standout, not sure if its the font size or colors on the existing label. It is very important to have on the label that this is a Premium Full Spectrum Hemp Oil that is 2000mg. Then after the label is redesigned and approved, I would need to packaging to be designed to match the approved label design.
This Hemp oil has a relaxing effect to help ease mental and emotional stress, tension and worry. The Omega Fatty Acids it contains also naturally improves your mood and overall brain function, causing you to feel more alert and focused. Hemp Oil helps with insomnia. Take some 2-3 hours before bedtime, you will feel relaxed yet aware of how tired you are that it will lead to a good night's sleep. Hemp Oil helps ease chronic pain and inflammation from conditions such as arthritis, fibromyalgia, lupus, and MS. As a pain relief supplement, it is a safer, natural, non-chemical and non-addictive alternative to prescription painkillers.

Target Market(s)

Adults

Industry/Entity Type

Supplement

Font styles to use
Serif
Sans Serif

Colors

Designer to choose colors to be used in the design.

Requirements
Must have
• All information thats on current label but where it says 750 in the front of the existing label, it needs to say 2000. The 2000 should be prominent on the label.

```html
<!DOCTYPE html>
<html lang="en">
<head>
<meta charset="utf-8">
<title>Marbleleaf Hemp – Tincture Label</title>
<link href="https://fonts.googleapis.com/css2?family=Oswald:wght@400;500;600;700&display=swap" rel="stylesheet">
<style>
  :root {
    --canvas: #e9e9e9;
    --leaf-dark: #1f5a22;
    --leaf-mid: #2f7a2c;
    --leaf-light: #4e9a3a;
    --panel: #ffffff;
    --gold-dark: #9a6a12;
    --gold: #c8921e;
    --gold-light: #e8c25a;
    --ink: #1a1a1a;
    --tag: #9ebd8e;
    --tag-ink: #ffffff;
    --mark: #8fae86;
  }
  * { box-sizing: border-box; margin: 0; padding: 0; }
  html, body { width: 1200px; height: 1200px; overflow: hidden; }
  body {
    background: radial-gradient(circle at 50% 45%, #f7f7f7 0%, var(--canvas) 75%);
    font-family: "Oswald", "Arial Narrow", sans-serif;
    display: flex; align-items: center; justify-content: center;
  }
  .label {
    position: relative;
    width: 680px; height: 960px;
    overflow: hidden;
  }
  .label-backdrop {
    position: absolute; inset: 0;
    background:
      radial-gradient(circle at 30% 25%, var(--leaf-light) 0%, transparent 45%),
      radial-gradient(circle at 75% 70%, var(--leaf-light) 0%, transparent 40%),
      linear-gradient(160deg, var(--leaf-mid) 0%, var(--leaf-dark) 100%);
  }
  .info-panel {
    position: absolute;
    left: 70px; top: 170px; width: 540px; height: 690px;
    background: var(--panel);
    border: 12px solid var(--gold);
    border-image: linear-gradient(135deg, var(--gold-light), var(--gold-dark) 40%, var(--gold-light) 60%, var(--gold-dark)) 1;
    display: flex; flex-direction: column; align-items: center;
    padding-top: 48px;
    text-align: center;
  }
  .brand-mark {
    display: flex; align-items: center; gap: 10px;
    color: var(--mark); font-weight: 500; font-size: 22px; letter-spacing: 2px;
    text-transform: uppercase;
  }
  .brand-mark .dot {
    width: 18px; height: 18px; border-radius: 50%; background: var(--mark);
  }
  .product-name {
    margin-top: 40px;
    font-weight: 600; font-size: 82px; line-height: 1.02; letter-spacing: 1px;
    text-transform: uppercase;
    background: linear-gradient(135deg, var(--gold-light), var(--gold-dark) 45%, var(--gold) 70%, var(--gold-dark));
    -webkit-background-clip: text; background-clip: text; color: transparent;
  }
  .spectrum {
    margin-top: 38px;
    font-weight: 500; font-size: 30px; color: var(--ink); letter-spacing: 0.5px;
  }
  .strength {
    margin-top: 4px;
    font-weight: 500; font-size: 30px; color: var(--ink);
    display: flex; align-items: baseline; gap: 10px;
  }
  .strength .mg {
    font-weight: 600; font-size: 54px; color: var(--gold);
  }
  .details {
    margin-top: 22px;
    font-weight: 500; font-size: 15px; color: var(--ink); line-height: 1.6;
  }
  .flavor-tag {
    margin-top: 30px;
    background: var(--tag); color: var(--tag-ink);
    font-weight: 500; font-size: 20px; letter-spacing: 0.5px;
    padding: 2px 10px;
  }
</style>
</head>
<body>
  <div class="label">
    <div class="label-backdrop" role="img" aria-label="Deep green backdrop scattered with hemp leaf pattern"></div>
    <div class="info-panel">
      <div class="brand-mark"><span class="dot"></span>Marbleleaf Hemp</div>
      <h1 class="product-name">Marbleleaf<br>Hemp</h1>
      <p class="spectrum">PREMIUM FULL SPECTRUM</p>
      <p class="strength"><span class="mg">2000</span>HEMP OIL</p>
      <p class="details">2000 MG DIETARY SUPPLEMENT<br>1 FL OZ ( 30ML)</p>
      <p class="flavor-tag">NATURAL PEPPERMINT FLAVOR</p>
    </div>
  </div>
</body>
</html>
```